Corporate Identity Design Project

Teslin Varrow Design is a small boutique event planning and floral design company, based in Northern Alberta. I require the creation of some corporate identity pieces. I want a minimalistic design.
Website www.teslinvarrow.example

Pieces should include
1. Business Card
Should include the company logo, name, email address, address, phone number. These will be professional printed.
These are three cards that I like:
http://cardsamplegallery.example/wp-content/uploads/2010/02/Odile_Vantreck_Roomworks_by_Pepperleaf_studio_Media.jpg
http://neatcardshowcase.example/wp-content/uploads/2011/06/Quiet-Studio-Minimalist-Business-Cards_11.jpg
http://graphicfeedhub.example/wp-content/uploads/2012/03/16.minimalist-business-cards.jpg
I like letterpress, but I am open to other options.

2. Letterhead
will be professionally printed

3. Envelope

4. Fax Sheet
will be printed on home printer

5. Pocket Presentation
Like -http://wrenfieldgardens.example/img/design_step_proposal@2x.jpg

6. Invoice
Like - http://samplehost.example/quillmarsh/2011/02/falcon-athletics-4-letterhead-combined.png?w=529

7. Proposal
Like something like this – this will not be printed, but rather emailed to clients
Like http://files7.imagedepot.example/getfile/files.imagedepot.example/trelvo-studio/nkuBfi2LVj7ENiUb5D16wqAHQHqNNT5vut7mukSTmisfoGHYXGEv9haEQOPL/Picture-52.png.scaled.500.jpg

8. Contract
Like http://www.brightkeyadvertising.example/images/sample-contract.jpg

9. Business Brochure – I have removed this piece from the project and will most likely post it as another project at a later date.

If you think that this is a project of interest to you, but feel that it is “too much” work for the price, please let me know how you would re-package it – I am open to suggestions.

Target Market(s)

Young women

Industry/Entity Type

Boutique

Requirements
Should not have
• I do not want it to look "frilly"

```html
<!DOCTYPE html>
<html lang="en">
<head>
<meta charset="utf-8">
<title>Teslin Varrow Design — Stationery Set</title>
<link rel="stylesheet" href="https://fonts.googleapis.com/css2?family=Open+Sans:wght@400;600;700&display=swap">
<style>
  :root {
    --charcoal: #3a3638;
    --rose: #c07878;
    --ink: #4a4648;
    --paper: #ffffff;
    --edge: #9a9a9a;
  }
  * { box-sizing: border-box; margin: 0; padding: 0; }
  html, body {
    width: 1180px; height: 1200px; overflow: hidden;
    background: var(--paper);
    font-family: "Open Sans", Arial, sans-serif;
    color: var(--ink);
  }
  .set { position: relative; width: 1180px; height: 1200px; }

  .sheet { position: absolute; overflow: hidden; background: var(--paper); }
  .sheet > svg.art { position: absolute; inset: 0; width: 100%; height: 100%; }

  .letterhead { left: 0; top: 0; width: 834px; height: 1200px; border: 1px solid var(--edge); }
  .envelope { left: 200px; top: 603px; width: 960px; height: 461px; border: 1px solid var(--edge); }
  .business-card {
    left: 296px; top: 318px; width: 400px; height: 190px;
    overflow: visible; background: transparent;
    transform: rotate(-10deg);
  }

  .wordmark { position: absolute; display: flex; align-items: center; gap: 12px; }
  .wordmark .mark { border-radius: 50%; background: var(--rose); flex: none; }
  .wordmark .name {
    font-weight: 600; color: var(--ink); text-transform: uppercase;
    letter-spacing: 0.16em; line-height: 1.15;
  }

  .letterhead .wordmark { left: 50px; top: 46px; }
  .letterhead .mark { width: 60px; height: 60px; }
  .letterhead .name { font-size: 15px; }

  .business-card .wordmark { left: 26px; top: 50px; }
  .business-card .mark { width: 46px; height: 46px; }
  .business-card .name { font-size: 12px; }

  .envelope .wordmark { left: 94px; top: 74px; gap: 16px; }
  .envelope .mark { width: 84px; height: 84px; }
  .envelope .name { font-size: 19px; }

  .contact { position: absolute; list-style: none; }
  .contact li { display: flex; align-items: center; gap: 8px; white-space: nowrap; }
  .contact svg { width: 10px; height: 10px; flex: none; }
  .contact .web { font-weight: 700; }

  .letterhead .contact { left: 560px; top: 1110px; color: var(--paper); font-size: 14px; line-height: 20px; }
  .letterhead .contact svg { fill: var(--paper); }

  .business-card .contact { right: 18px; bottom: 14px; color: var(--paper); font-size: 11px; line-height: 15px; }
  .business-card .contact svg { fill: var(--paper); width: 8px; height: 8px; }

  .envelope .contact { left: 120px; bottom: 22px; color: var(--ink); font-size: 15px; line-height: 20px; }
  .envelope .contact svg { fill: var(--ink); }
</style>
</head>
<body>
<svg width="0" height="0" style="position:absolute" aria-hidden="true">
  <defs>
    <radialGradient id="glow-top" cx="130" cy="80" r="260" gradientUnits="userSpaceOnUse">
      <stop offset="0" stop-color="#ffffff"/>
      <stop offset="0.35" stop-color="#e6e6e6"/>
      <stop offset="1" stop-color="#3a3638"/>
    </radialGradient>
    <radialGradient id="glow-card" cx="90" cy="80" r="220" gradientUnits="userSpaceOnUse">
      <stop offset="0" stop-color="#ffffff"/>
      <stop offset="0.35" stop-color="#dcdcdc"/>
      <stop offset="1" stop-color="#3a3638"/>
    </radialGradient>
    <symbol id="i-pin" viewBox="0 0 10 10"><path d="M5 0a3.4 3.4 0 0 1 3.4 3.4C8.4 6 5 10 5 10S1.6 6 1.6 3.4A3.4 3.4 0 0 1 5 0z"/></symbol>
    <symbol id="i-phone" viewBox="0 0 10 10"><path d="M3 0h2v3H3.8c0 1.5.4 3 1.2 4H6v3H4C2.6 8.6 2 6.6 2 5S2.6 1.4 3 0z"/></symbol>
    <symbol id="i-mail" viewBox="0 0 10 10"><path d="M0 2h10v6H0zM1 3v.3l4 2.5 4-2.5V3z"/></symbol>
    <symbol id="i-web" viewBox="0 0 10 10"><circle cx="5" cy="5" r="4.5"/></symbol>
  </defs>
</svg>

<main class="set">
  <section class="sheet letterhead" aria-label="Letterhead">
    <svg class="art" viewBox="0 0 834 1200" preserveAspectRatio="none" aria-hidden="true">
      <path fill="var(--rose)" d="M0 0H834V185C720 150 600 118 470 132 330 150 190 180 0 168Z"/>
      <path fill="url(#glow-top)" d="M0 0H834V158C720 128 590 108 460 122 320 140 180 170 0 156Z"/>
      <path fill="var(--rose)" d="M290 1200C420 1118 600 1086 834 1088V1200Z"/>
    </svg>
    <div class="wordmark">
      <span class="mark"></span>
      <span class="name">Teslin<br>Varrow<br>Design</span>
    </div>
    <ul class="contact">
      <li><svg><use href="#i-pin"/></svg>Fernhollow, Northreach, Canada.</li>
      <li><svg><use href="#i-phone"/></svg>000 000 0000</li>
      <li><svg><use href="#i-mail"/></svg>hello@teslinvarrow.example</li>
      <li class="web"><svg><use href="#i-web"/></svg>www.teslinvarrow.example</li>
    </ul>
  </section>

  <section class="sheet business-card" aria-label="Business card">
    <svg class="art" viewBox="0 0 400 190" aria-hidden="true" style="overflow:visible">
      <path fill="var(--rose)" d="M0 0H340A66 66 0 0 1 406 66V190H66A66 66 0 0 1 -2 124Z" transform="translate(2 4)"/>
      <path fill="url(#glow-card)" d="M0 0H334A66 66 0 0 1 400 66V190H66A66 66 0 0 1 0 124Z"/>
    </svg>
    <div class="wordmark">
      <span class="mark"></span>
      <span class="name">Teslin<br>Varrow<br>Design</span>
    </div>
    <ul class="contact">
      <li><svg><use href="#i-pin"/></svg>Fernhollow, Northreach, Canada.</li>
      <li><svg><use href="#i-phone"/></svg>000 000 0000</li>
      <li><svg><use href="#i-mail"/></svg>hello@teslinvarrow.example</li>
      <li class="web"><svg><use href="#i-web"/></svg>www.teslinvarrow.example</li>
    </ul>
  </section>

  <section class="sheet envelope" aria-label="Envelope">
    <svg class="art" viewBox="0 0 960 461" preserveAspectRatio="none" aria-hidden="true">
      <path fill="var(--rose)" d="M0 0H90C70 60 64 120 72 200 80 280 90 380 86 461H0Z"/>
      <path fill="var(--charcoal)" d="M0 0H82C62 60 56 120 64 200 72 280 82 380 78 461H0Z"/>
    </svg>
    <div class="wordmark">
      <span class="mark"></span>
      <span class="name">Teslin<br>Varrow<br>Design</span>
    </div>
    <ul class="contact">
      <li><svg><use href="#i-pin"/></svg>Fernhollow, Northreach, Canada.</li>
      <li><svg><use href="#i-phone"/></svg>000 000 0000</li>
      <li><svg><use href="#i-mail"/></svg>hello@teslinvarrow.example</li>
      <li class="web"><svg><use href="#i-web"/></svg>www.teslinvarrow.example</li>
    </ul>
  </section>
</main>
</body>
</html>
```